Brindle Children's Center - Child Care brochure

I just bought a new child care and completely renovated the space. We are also designing a new website, so I need the brochure to match that with updated info. www.brindlechildrenscenter.com - Information on there is current. We expect to have the new one up and running in the next few days. We have new photo's that I'd like to be added to the flyer too. ps. the boys in the pictures are mine, so i would appreciate one of them being added :). support@pixelhavenweb.com has details on the website (dev.brindlechildrenscenter.com). The child care program is only open during the ski season - i.e. a resort facility catering to high end clients.
I'm attaching the the website information, the flyer I created, logo files and pictures.

dev.brindlechildrenscenter.com Added Sunday, September 24, 2017

Target Market(s)

Parents of young children

Font styles to use
Other font styles liked:
• "Things we said" & "Calibri Light"

Colors
cfeae6
fef1ee

Requirements
Must have
• Pictures of children. sleek design - winter, mountain theme. Check with website designer on new website.
Nice to have
• prices included
Should not have
• Kid like artwork

```html
<!DOCTYPE html>
<html lang="en">
<head>
<meta charset="utf-8">
<title>Brindle Children's Center – Flyer</title>
<link rel="stylesheet" href="https://fonts.googleapis.com/css2?family=Montserrat:wght@300;400;500;600;700&family=Kaushan+Script&display=swap">
<style>
  :root {
    --teal: #a3dbd4;
    --teal-soft: #cfeae6;
    --wine: #7d161b;
    --paper: #e4e7eb;
    --white: #ffffff;
    --ink: #2b2b2b;
    --hero-tint: rgba(118, 96, 118, 0.55);
    --sans: "Montserrat", Arial, sans-serif;
    --script: "Kaushan Script", cursive;
  }
  * { box-sizing: border-box; margin: 0; padding: 0; }
  html, body { width: 1000px; height: 1200px; overflow: hidden; }
  body { background: var(--paper); font-family: var(--sans); color: var(--ink); }

  .flyer { position: relative; width: 1000px; height: 1200px; background: var(--paper); }

  /* Hero */
  .hero-photo {
    position: absolute; left: 0; top: 0; width: 1000px; height: 402px;
    background: linear-gradient(180deg, #9aa6b8 0%, #c9d0da 35%, #e9edf2 70%, #f4f6f8 100%);
  }
  .hero-panel {
    position: absolute; left: 46px; top: 0; width: 908px; height: 402px;
    background: var(--hero-tint);
    text-align: center; color: var(--white);
  }
  .hero-kicker {
    position: absolute; top: 108px; left: 0; right: 0;
    font-weight: 300; font-size: 34px; letter-spacing: 2px; margin-left: -40px;
  }
  .hero-title {
    position: absolute; top: 142px; left: 0; right: 0;
    font-family: var(--script); color: var(--wine); font-size: 66px; margin-left: -20px;
  }
  .hero-copy {
    position: absolute; top: 262px; left: 100px; right: 100px;
    font-size: 12.5px; line-height: 1.45; font-weight: 400;
  }
  .brand-badge {
    position: absolute; left: 693px; top: 45px; width: 144px; height: 144px;
    border-radius: 50%; background: var(--white);
    display: flex; align-items: center; justify-content: center; text-align: center;
    font-family: var(--sans); font-weight: 700; font-size: 15px; line-height: 1.25;
    color: var(--wine); padding: 18px;
  }

  /* Tiles */
  .tile { position: absolute; }
  .tile-teal { background: var(--teal); }
  .photo { position: absolute; }
  .frame-label {
    position: absolute; border: 1.5px solid var(--white);
    display: flex; align-items: center; justify-content: center;
    font-family: var(--script); color: var(--white); font-size: 34px; line-height: 1;
    text-align: center;
  }
  .price-box { text-align: center; color: var(--ink); }
  .price-note { font-size: 12.5px; line-height: 1.35; font-weight: 400; }
  .price-note.strong { font-weight: 600; font-size: 13px; }
  .price-frame {
    display: inline-block; border: 1.5px solid var(--white);
    padding: 10px 14px; font-weight: 700; font-size: 27px; margin-top: 4px;
  }
  .price-frame.tall { padding: 14px 14px; margin-top: 10px; }

  /* Ski pass block */
  .pass-title { position: absolute; left: 22px; top: 24px; color: var(--wine); font-weight: 700; font-size: 21px; letter-spacing: .5px; }
  .pass-sub { position: absolute; left: 22px; top: 50px; font-size: 15px; }
  .diamond { position: absolute; width: 110px; height: 110px; }
  .diamond .shape {
    position: absolute; left: 17px; top: 17px; width: 76px; height: 76px;
    transform: rotate(45deg);
  }
  .diamond.solid .shape { background: var(--wine); }
  .diamond.outline .shape { border: 1.5px solid var(--white); }
  .diamond .label {
    position: absolute; inset: 0; display: flex; flex-direction: column;
    align-items: center; justify-content: center; line-height: 1.1;
  }
  .diamond .amount { font-weight: 700; font-size: 16px; }
  .diamond .range { font-size: 9.5px; }
  .diamond.solid .label { color: var(--white); }
  .diamond.outline .label { color: var(--wine); }
  .diamond.outline .range { color: var(--ink); }

  /* Info strip */
  .info-heading { color: var(--wine); font-weight: 700; font-size: 16px; margin-bottom: 6px; }
  .info-text { font-size: 12.5px; line-height: 1.35; }
  .info-divider { position: absolute; left: 270px; top: 30px; width: 1px; height: 36px; background: #6a6a6a; }

  /* Footer */
  .contact-band {
    position: absolute; left: 46px; top: 1089px; width: 908px; height: 84px;
    background: var(--wine); color: var(--white);
  }
  .contact-heading { position: absolute; left: 10px; top: 12px; font-weight: 700; font-size: 16px; }
  .contact-lines { position: absolute; left: 10px; top: 48px; font-size: 12.5px; line-height: 1.35; }
  .contact-right { position: absolute; right: 26px; top: 48px; font-size: 11.5px; line-height: 1.45; }
</style>
</head>
<body>
<main class="flyer">

  <!-- Hero -->
  <div class="hero-photo" role="img" aria-label="Snowy ski mountain slopes with the lodge and skiers"></div>
  <section class="hero-panel">
    <p class="hero-kicker">COME AND</p>
    <h1 class="hero-title">Have Fun</h1>
    <p class="hero-copy">When you hit the slopes you want to make sure your child has a great day too.<br>
      At the Brindle Children's Center you can be sure that your child receives the best care possible –<br>
      and has a great time to boot! Located on the slopes of world famous Pinecrest Ski Resort,<br>
      you can drop your child at a safe, and fun center and step out the door to the slopes.</p>
  </section>
  <div class="brand-badge">Brindle Children's Center</div>

  <!-- Full day -->
  <div class="tile" style="left:46px; top:414px; width:274px; height:141px;">
    <div class="photo" style="inset:0; background:linear-gradient(135deg,#6f5a4e,#b9a28a 55%,#d9cbb8);" role="img" aria-label="Two children playing with a wooden puzzle"></div>
    <div class="frame-label" style="left:22px; top:50px; width:232px; height:56px;">Full day</div>
  </div>
  <div class="tile tile-teal price-box" style="left:46px; top:555px; width:274px; height:145px; padding-top:40px;">
    <p class="price-note">(8:30 AM - 4:30 PM)</p>
    <span class="price-frame">$190</span>
  </div>

  <!-- Half day -->
  <div class="tile tile-teal price-box" style="left:366px; top:414px; width:272px; height:141px; padding-top:30px;">
    <span class="price-frame" style="padding:6px 14px;">$ 89</span>
    <p class="price-note">(8:30 am - 12:30 pm)<br>(12:30 am - 4:30 pm)</p>
  </div>
  <div class="tile" style="left:366px; top:555px; width:272px; height:145px;">
    <div class="photo" style="inset:0; background:linear-gradient(135deg,#c5726e,#a98d86 50%,#6f7f9a);" role="img" aria-label="Children reading picture books in the playroom"></div>
    <div class="frame-label" style="left:18px; top:48px; width:234px; height:56px;">Half day</div>
  </div>

  <!-- 5 Day packages -->
  <div class="tile" style="left:681px; top:414px; width:273px; height:141px;">
    <div class="photo" style="inset:0; background:linear-gradient(135deg,#e9e4dc,#c9a679 50%,#8e6a45);" role="img" aria-label="Large teddy bear sitting with storybooks"></div>
    <div class="frame-label" style="left:22px; top:28px; width:234px; height:86px; flex-direction:column; font-size:30px;">5<br>Day Packages</div>
  </div>
  <div class="tile tile-teal price-box" style="left:681px; top:555px; width:273px; height:145px; padding-top:40px;">
    <p class="price-note strong">THAT'S A $50 SAVING!</p>
    <span class="price-frame">$1495</span>
  </div>

  <!-- Season pass -->
  <section class="tile tile-teal" style="left:46px; top:709px; width:592px; height:272px;">
    <h2 class="pass-title">NEW SEASON SKI</h2>
    <p class="pass-sub">Pass child care package</p>

    <div class="diamond outline" style="left:76px; top:86px;">
      <span class="shape"></span>
      <div class="label"><span class="amount">$2,700</span><span class="range">41 - 60</span><span class="range">Full Days</span></div>
    </div>
    <div class="diamond solid" style="left:213px; top:81px;">
      <span class="shape"></span>
      <div class="label"><span class="amount">$900</span><span class="range">01 - 20</span><span class="range">Full Days</span></div>
    </div>
    <div class="diamond solid" style="left:17px; top:142px;">
      <span class="shape"></span>
      <div class="label"><span class="amount">$3,600</span><span class="range">60 - 80</span><span class="range">Full Days</span></div>
    </div>
    <div class="diamond outline" style="left:141px; top:153px;">
      <span class="shape"></span>
      <div class="label"><span class="amount">$1,800</span><span class="range">21 - 40</span><span class="range">Full Days</span></div>
    </div>

    <div class="photo" style="left:320px; top:91px; width:272px; height:181px; background:linear-gradient(135deg,#6a4a46,#b08b80 45%,#cdb8a8);" role="img" aria-label="Two children working on a puzzle at a table"></div>
    <div class="frame-label" style="left:342px; top:142px; width:228px; height:72px; font-size:26px; border-color:var(--wine);">Pass child<br>care package</div>
  </section>

  <!-- Après-ski -->
  <div class="tile" style="left:681px; top:709px; width:273px; height:219px;">
    <div class="photo" style="inset:0; background:linear-gradient(135deg,#e8e2dc,#c8b9a8 50%,#6f9aa8);" role="img" aria-label="Toddler playing with soft toys"></div>
    <div class="frame-label" style="left:18px; top:94px; width:246px; height:58px;">Après-ski Care</div>
  </div>
  <div class="tile tile-teal price-box" style="left:681px; top:928px; width:273px; height:153px; padding-top:24px;">
    <p class="price-note strong">FRIDAY AND SATURDAY ONLY</p>
    <p class="price-note">(4:30 PM- 6:30 PM)</p>
    <span class="price-frame tall">$1,495</span>
  </div>

  <!-- Info strip -->
  <section class="tile tile-teal" style="left:46px; top:989px; width:592px; height:92px; padding:14px 10px;">
    <div style="position:absolute; left:10px; top:12px; width:240px;">
      <h3 class="info-heading">OPEN</h3>
      <p class="info-text">Our child care center will be open, under new ownership,</p>
    </div>
    <span class="info-divider"></span>
    <div style="position:absolute; left:330px; top:12px; width:250px;">
      <h3 class="info-heading">BRINDLE CHILDREN CENTER</h3>
      <p class="info-text">for the 2017/2018 ski season on the 3rd floor of the Summit Ski Ticket Office.</p>
    </div>
  </section>

  <!-- Contact -->
  <footer class="contact-band">
    <h3 class="contact-heading">CONTAC US</h3>
    <p class="contact-lines">801 555 0142<br>fun@brindlechildrenscenter.com</p>
    <p class="contact-right">NEW season ski pass packages &amp; après-ski child care available<br>www.brindlechildrenscenter.com</p>
  </footer>

</main>
</body>
</html>
```